Meridale Eating needs Stationary and a business card

We would like to use our current logo. The text can be moved around as needed. The stationary needs to be a 'first page' where the logo is more prominent to be impressive on higher quality paper and a second page where the logo is more subtle where there will be much more information on the page. There are 2 clinic locations which will need include name, address, phone number, fax number, web address. The business card should be single sided and contain this information also.
The design must be contemporary and sophisticated as this is a science based diet run out of a medical clinic.

Target Market(s)

People wanting to lose weight, athletes looking to optimise performance, people with arthritis or fighting cancer

Industry/Entity Type

Business

Contact Information for Business Card

must use the logo. I have attached an example card with the practice details on it. there must be space for the doctors name. Also the website www.meridaleeating.example.au

Requirements
Must have
• the logo, the business adresses and phone numbers, the website, the doctors name and qualifications
Nice to have
• some creativity
Should not have
• Do not simply reproduce the existing card please

```html
<!DOCTYPE html>
<html lang="en">
<head>
<meta charset="utf-8">
<title>Meridale Eating – Business Card</title>
<link rel="stylesheet" href="https://fonts.googleapis.com/css2?family=Lato:wght@300;400;700&display=swap">
<style>
  :root {
    --page-bg: #e6e7e9;
    --card-bg: #f7f7f6;
    --ink: #4a4a4a;
    --ink-soft: #6d6d6d;
    --navy-blue: #3a68a6;
    --sky-cyan: #46c1df;
  }
  * { box-sizing: border-box; margin: 0; padding: 0; }
  html, body {
    width: 1200px; height: 900px; overflow: hidden;
    background: var(--page-bg);
    font-family: "Lato", sans-serif;
    color: var(--ink);
  }
  .business-card {
    position: absolute; left: 100px; top: 145px;
    width: 1000px; height: 610px;
    background: var(--card-bg);
    box-shadow: 0 6px 24px rgba(0,0,0,0.12);
    overflow: hidden;
  }
  .brand {
    position: absolute; left: 70px; top: 150px;
    display: flex; align-items: center; gap: 18px;
  }
  .brand-dot {
    width: 86px; height: 86px; border-radius: 50%;
    background: var(--sky-cyan);
  }
  .brand-name {
    font-weight: 700; font-size: 34px; letter-spacing: 0.5px;
    color: var(--navy-blue); text-transform: uppercase; line-height: 1.05;
    width: 220px;
  }
  .doctor {
    position: absolute; left: 470px; top: 120px;
  }
  .doctor-name { font-weight: 700; font-size: 54px; color: #3f3f3f; line-height: 1.1; }
  .doctor-quals { font-weight: 300; font-size: 19px; color: var(--ink-soft); margin-top: 6px; }
  .doctor-role { font-weight: 400; font-size: 32px; color: var(--sky-cyan); margin-top: 2px; }
  .clinic {
    position: absolute; font-size: 22px; line-height: 1.32; font-weight: 300;
  }
  .clinic-ashmere { left: 390px; top: 300px; }
  .clinic-coralby { left: 680px; top: 345px; }
  .clinic-name, .clinic-speciality { font-weight: 700; color: #3a3a3a; }
  .clinic-contact { margin-top: 8px; }
  .clinic-speciality { margin-top: 8px; }
  .band { position: absolute; bottom: 0; }
  .band-navy { left: 0; width: 400px; height: 52px; background: var(--navy-blue); }
  .band-cyan { left: 410px; right: 0; height: 30px; background: var(--sky-cyan); }
</style>
</head>
<body>
  <main class="business-card">
    <div class="brand">
      <span class="brand-dot"></span>
      <span class="brand-name">Meridale Eating</span>
    </div>

    <header class="doctor">
      <h1 class="doctor-name">Dr Adrian Kessel</h1>
      <p class="doctor-quals">MBBS (NSW) MBiomedE FRACS (Ortho) FAOrthA</p>
      <p class="doctor-role">Orthopaedic Surgeon</p>
    </header>

    <section class="clinic clinic-ashmere">
      <p class="clinic-name">Ashmere</p>
      <p>21-23 Harlow Road</p>
      <p>Ashmere NSW 2140</p>
      <p class="clinic-contact">Tel: 02 9000 1482</p>
      <p>Fax: 02 9000 1483</p>
      <p class="clinic-speciality">Shoulder and Elbow</p>
      <p>www.akessel.example.au</p>
    </section>

    <section class="clinic clinic-coralby">
      <p class="clinic-name">Coralby</p>
      <p>88 Linden Road</p>
      <p>Coralby NSW 2035</p>
      <p class="clinic-contact">Tel: 02 9000 2716</p>
      <p>Fax: 02 9000 2717</p>
      <p class="clinic-speciality">Knee Surgery</p>
      <p>www.kneeclinic.example.au</p>
    </section>

    <div class="band band-navy"></div>
    <div class="band band-cyan"></div>
  </main>
</body>
</html>
```